Awesome new bottle needs Awesome new label

We need an awesome label design for our new bottle. It is a square bottle with 4 flat surfaces for the label. These surfaces make it easier to play with transparent labels.
The water comes from the Mount Kelvara Springs. Themes that we want to concentrate on are purity of the water as well as the clarity of the bottle. Think Quenor's new label design for inspiration. I am looking for something like that. I have attached pictures of the bottle as well as the schematics of the label.
The brand to be used is "Brumelle", which means Solar in French. I would like transparent labels as the smooth surfaces make good areas to play with this idea.
Thanks and good luck!
Tav
Reason: Waiting for the final designs from my shortlisted designers

```html
<!DOCTYPE html>
<html lang="en">
<head>
<meta charset="utf-8">
<title>Brumelle — Label Design</title>
<link rel="stylesheet" href="https://fonts.googleapis.com/css2?family=Montserrat:wght@400;600;800&family=Lora:wght@400&display=swap">
<style>
  :root {
    --bg-top: #dfeaf4;
    --bg-bottom: #c2d8ec;
    --brand-blue: #1f5fa8;
    --deep-blue: #163d6e;
    --table-blue: #3f7fc4;
    --table-line: #ffffff;
    --label-tint: rgba(214, 232, 248, 0.85);
    --ink-dark: #2b2b2b;
    --ink-mid: #4a5561;
    --white: #ffffff;
  }
  * { box-sizing: border-box; margin: 0; padding: 0; }
  html, body { width: 1200px; height: 1000px; overflow: hidden; }
  body {
    position: relative;
    background: linear-gradient(180deg, var(--bg-top) 0%, var(--bg-bottom) 100%);
    font-family: "Montserrat", sans-serif;
  }

  .brand-header { position: absolute; left: 910px; top: 72px; width: 260px; text-align: center; }
  .brand-name { font-weight: 800; font-size: 48px; color: var(--brand-blue); line-height: 1; }
  .brand-tagline { font-family: "Lora", serif; font-size: 13px; color: var(--deep-blue); margin-top: 4px; }
  .spec-title { position: absolute; left: 965px; top: 172px; font-size: 21px; font-weight: 600; color: var(--ink-dark); letter-spacing: 0.5px; }
  .spec-title span { color: var(--brand-blue); }
  .spec-size { position: absolute; left: 968px; top: 198px; font-size: 12px; color: var(--ink-mid); }

  .label {
    position: absolute; top: 445px; width: 240px; height: 188px;
    background: var(--label-tint); overflow: hidden;
  }
  .label--front { left: 62px; }
  .label--back {
    left: 385px;
    background: linear-gradient(180deg, rgba(214,232,248,0.9) 0%, rgba(170,203,234,0.9) 100%);
  }
  .label--facts { left: 720px; background: transparent; overflow: visible; }

  .sunburst {
    position: absolute; left: 0; top: 0; width: 100%; height: 130px;
    background: radial-gradient(circle at 50% 35%, #ffffff 0%, #d4e6f6 40%, #9fc2e4 100%);
  }
  .splash {
    position: absolute; left: 0; bottom: 0; width: 100%; height: 50px;
    background: linear-gradient(180deg, rgba(120,170,220,0) 0%, #6fa6dc 60%, #3f7fc4 100%);
  }
  .splash--side { left: auto; right: 0; width: 70px; height: 70px; bottom: 20px;
    background: radial-gradient(ellipse at 60% 50%, #7fb1e1 0%, rgba(127,177,225,0) 70%); }

  .label-logo { position: absolute; width: 100%; text-align: center; }
  .label-logo .name { font-weight: 800; color: var(--brand-blue); line-height: 1; }
  .label-logo .line { font-family: "Lora", serif; color: var(--deep-blue); }
  .label--front .label-logo { top: 66px; }
  .label--front .name { font-size: 36px; }
  .label--front .line { font-size: 10px; margin-top: 2px; }
  .label--back .label-logo { top: 44px; }
  .label--back .name { font-size: 30px; }
  .label--back .line { font-size: 9px; margin-top: 2px; }

  .product-type {
    position: absolute; top: 130px; width: 100%; text-align: center;
    font-family: "Lora", serif; font-size: 10px; color: var(--deep-blue);
    letter-spacing: 0.5px; line-height: 1.3; text-transform: uppercase;
  }

  .origin-copy {
    position: absolute; left: 30px; top: 118px; font-size: 6.5px; color: var(--deep-blue);
    line-height: 1.45; text-transform: uppercase;
  }
  .origin-copy p + p { margin-top: 6px; }
  .origin-copy .company { font-weight: 600; font-size: 7.5px; }

  .facts {
    position: absolute; left: 15px; top: 15px; width: 170px;
    background: var(--table-blue); border-radius: 4px; padding: 4px 6px 5px;
    color: var(--white);
  }
  .facts-title { font-weight: 800; font-size: 14px; letter-spacing: 0.3px; line-height: 1.2; }
  .facts-serving { font-size: 8px; border-top: 1px solid var(--table-line); border-bottom: 3px solid var(--table-line); padding: 1px 0; }
  .facts-note { font-size: 4.5px; border-bottom: 1px solid var(--table-line); padding: 1px 0; }
  .facts-table { width: 100%; border-collapse: collapse; font-size: 5px; line-height: 1.2; }
  .facts-table td { border-bottom: 0.5px solid rgba(255,255,255,0.6); padding: 0.5px 0; vertical-align: top; }
  .facts-table td:nth-child(2) { width: 34px; }
  .facts-table td:nth-child(3) { width: 16px; text-align: right; }
  .facts-table.minerals { border-top: 3px solid var(--table-line); margin-top: 4px; }
  .facts-table tr:last-child td { border-bottom: none; }
</style>
</head>
<body>
  <header class="brand-header">
    <div class="brand-name">Brumelle</div>
    <div class="brand-tagline">from the Mount Kelvara Springs</div>
  </header>
  <div class="spec-title">LABEL <span>DESIGN</span></div>
  <div class="spec-size">57MM X 45MM &nbsp;(228 X 45)</div>

  <section class="label label--front">
    <div class="sunburst" role="img" aria-label="Sun rising over snowy mountains with radiating light rays"></div>
    <div class="splash" role="img" aria-label="Clear water splash with bubbles"></div>
    <div class="label-logo">
      <div class="name">Brumelle</div>
      <div class="line">from the Mount Kelvara Springs</div>
    </div>
    <div class="product-type">Natural<br>Mineral Water</div>
  </section>

  <section class="label label--back">
    <div class="splash splash--side" role="img" aria-label="Clear water splash"></div>
    <div class="label-logo">
      <div class="name">Brumelle</div>
      <div class="line">from the Mount Kelvara Springs</div>
    </div>
    <div class="origin-copy">
      <p>Sourced and bottled at the<br>Kelvara Mountain Springs</p>
      <p>Manufactured for and imported by:<br><span class="company">Norvane Trading Pte Ltd</span><br>48 Harlow Quay Road, Singapore 049812<br>Tel: +6560001234</p>
    </div>
  </section>

  <section class="label label--facts">
    <div class="facts">
      <div class="facts-title">NUTRITION FACTS</div>
      <div class="facts-serving">SERVING SIZE 1000 ML</div>
      <div class="facts-note">AMOUNT PER SERVING (MG/L)</div>
      <table class="facts-table">
        <tr><td>ENERGY</td><td>0.0K</td><td></td></tr>
        <tr><td>TOTAL FAT</td><td>0.0G</td><td>0%</td></tr>
        <tr><td>PROTEIN</td><td>0.0G</td><td>0%</td></tr>
        <tr><td>CARBOHYDRATE</td><td>0.0G</td><td>0%</td></tr>
      </table>
      <table class="facts-table minerals">
        <tr><td>BICARBONATE</td><td>103.00</td><td></td></tr>
        <tr><td>CALCIUM</td><td>8.90</td><td></td></tr>
        <tr><td>SODIUM</td><td>18.00</td><td></td></tr>
        <tr><td>CHLORIDES</td><td>&lt; 3.20</td><td></td></tr>
        <tr><td>SULPHATES</td><td>11.10</td><td></td></tr>
        <tr><td>MAGNESIUM</td><td>10.00</td><td></td></tr>
        <tr><td>POTASSIUM</td><td>1.60</td><td></td></tr>
        <tr><td>pH AT SOURCE</td><td>7.72</td><td></td></tr>
        <tr><td>TOTAL DISSOLVED SOLIDS<br>AT 180°C</td><td>144</td><td></td></tr>
      </table>
    </div>
  </section>
</body>
</html>
```